Poster for List of Company Values

We need a poster to outline our Values which will be displayed in our office as well as posted on our website and other platforms (so need to allow for some flexibly in its application).

File attached outlines what we currently have with design and also our company style guide.

Note that we are looking for a modern, clean look, which still represents our core activities of construction and environmental services.

You can also reference our website here:

https://corvellagroup.com.au/

Happy to answer any questions you might have.

Thanks for your interest,
Wynn

Target Market(s)

Internal and External clients

Industry/Entity Type

Construction, water and recycling

Font styles to use
Sans Serif

Requirements
Must have
• All values on the one page. Graphic to represent each value. Also needs to use company logo
Nice to have
• Preference for poster to be orientated in landscape
Should not have
• Do not follow example provided, this is only to demonstrate what we have to date and also the text required

```html
<!DOCTYPE html>
<html lang="en">
<head>
<meta charset="utf-8">
<title>Corvella Group – Company Values Posters</title>
<link href="https://fonts.googleapis.com/css2?family=Montserrat:wght@400;500;700;800;900&display=swap" rel="stylesheet">
<style>
  :root{
    --stage:#dde8ee;
    --paper:#ffffff;
    --ink:#111111;
    --brand-navy:#1b3f8f;
    --brand-green:#3fae49;
    --soft-green:#cfe6c9;
    --soft-lilac:#b7b9dd;
    --v1:#1faa4b;
    --v2:#d39e2e;
    --v3:#0e3a8a;
    --v4:#f06623;
    --v5:#a84c9f;
    --v6:#2fa3db;
    --sky-top:#8fc3e6;
    --sky-mid:#e9d7b8;
    --site-warm:#9a6a3f;
    --site-dark:#4a3a2c;
  }
  *{box-sizing:border-box;margin:0;padding:0}
  html,body{width:1200px;height:769px;overflow:hidden}
  body{background:var(--stage);font-family:"Montserrat",Arial,sans-serif;color:var(--ink);position:relative}

  .poster{position:absolute;background:var(--paper);overflow:hidden;box-shadow:0 6px 18px rgba(20,40,60,.22)}
  .poster--portrait{left:116px;top:122px;width:342px;height:528px}
  .poster--landscape{left:536px;top:309px;width:529px;height:342px}

  .poster__deco{position:absolute;inset:0;width:100%;height:100%}

  .brand{position:absolute;display:flex;align-items:center;gap:6px}
  .brand__mark{width:16px;height:16px;background:var(--brand-navy);border-radius:50%}
  .brand__name{font-weight:800;color:#3a3a3a;line-height:.95}
  .poster--portrait .brand{left:14px;top:18px}
  .poster--portrait .brand__mark{width:22px;height:22px}
  .poster--portrait .brand__name{font-size:17px}
  .poster--landscape .brand{left:290px;top:22px}
  .poster--landscape .brand__name{font-size:12px}

  .tagline{position:absolute;background:var(--brand-green);color:#fff;font-weight:500;letter-spacing:.2px;
    clip-path:polygon(0 0,96% 0,100% 100%,0 100%);white-space:nowrap}
  .headline{position:absolute;font-weight:900;line-height:.95;letter-spacing:.3px;text-transform:uppercase}
  .intro{position:absolute;font-size:6.2px;line-height:1.35;color:#222;text-align:justify}

  .poster--portrait .tagline{left:0;top:91px;width:242px;height:14px;font-size:9.5px;padding:1px 0 0 12px}
  .poster--portrait .headline{left:13px;top:107px;font-size:24px}
  .poster--portrait .intro{left:14px;top:159px;width:270px}

  .poster--landscape .tagline{left:282px;top:231px;width:226px;height:13px;font-size:8.5px;padding:1px 0 0 7px}
  .poster--landscape .headline{left:289px;top:246px;font-size:21px}
  .poster--landscape .intro{left:289px;top:294px;width:219px}

  .value{position:absolute;left:0;width:100%}
  .value__pill{position:absolute;left:0;top:0;width:190px;height:100%;border-radius:0 26px 26px 0;color:#fff;
    display:flex;flex-direction:column;justify-content:center;padding:0 16px 0 12px}
  .value__title{font-weight:800;font-size:9.5px;line-height:.95;text-transform:uppercase;padding-right:28px}
  .value__text{font-size:6px;line-height:1.2;margin-top:2.5px;font-weight:500}
  .value__sub{font-size:5.6px;font-weight:800;margin-top:1.5px;text-transform:uppercase;line-height:1.1}
  .value__sub + .value__text{margin-top:0}
  .value__icon{position:absolute;right:20px;top:5px;width:20px;height:20px}
  .value__link{position:absolute;height:5px;border-radius:3px}
  .value__hook{position:absolute;width:10px;height:9px;border:2px solid #fff;border-right:none;border-radius:5px 0 0 5px}
  .value__badge{position:absolute;border-radius:50%;border:2.5px solid #fff;box-shadow:0 0 0 1.5px rgba(0,0,0,.06);
    display:flex;align-items:center;justify-content:center;color:#fff;font-weight:800}

  .poster--portrait .value{height:50px}
  .poster--portrait .value__link{left:178px;width:118px;top:22.5px}
  .poster--portrait .value__hook{left:180px;top:20.5px}
  .poster--portrait .value__badge{left:288px;top:4px;width:42px;height:42px;font-size:25px}

  .poster--landscape .value{height:48px}
  .poster--landscape .value__pill{padding:0 14px 0 23px}
  .poster--landscape .value__text{font-size:5.8px}
  .poster--landscape .value__icon{right:18px;top:6px;width:18px;height:18px}
  .poster--landscape .value__link{left:178px;width:50px;top:21.5px}
  .poster--landscape .value__hook{left:180px;top:19.5px}
  .poster--landscape .value__badge{left:219px;top:5px;width:40px;height:40px;font-size:23px}

  .tone-1 .value__pill,.tone-1 .value__link,.tone-1 .value__badge{background:var(--v1)}
  .tone-2 .value__pill,.tone-2 .value__link,.tone-2 .value__badge{background:var(--v2)}
  .tone-3 .value__pill,.tone-3 .value__link,.tone-3 .value__badge{background:var(--v3)}
  .tone-4 .value__pill,.tone-4 .value__link,.tone-4 .value__badge{background:var(--v4)}
  .tone-5 .value__pill,.tone-5 .value__link,.tone-5 .value__badge{background:var(--v5)}
  .tone-6 .value__pill,.tone-6 .value__link,.tone-6 .value__badge{background:var(--v6)}
</style>
</head>
<body>

<svg width="0" height="0" style="position:absolute" aria-hidden="true">
  <defs>
    <linearGradient id="site-photo" x1="0" y1="0" x2="0.3" y2="1">
      <stop offset="0" stop-color="var(--sky-top)"/>
      <stop offset=".4" stop-color="var(--sky-mid)"/>
      <stop offset=".7" stop-color="var(--site-warm)"/>
      <stop offset="1" stop-color="var(--site-dark)"/>
    </linearGradient>
    <symbol id="icon-flag" viewBox="0 0 24 24"><g fill="none" stroke="#fff" stroke-width="1.4" stroke-linejoin="round"><path d="M6 3v12M6 3h9l-2 3 2 3H6"/><rect x="3" y="14" width="8" height="7" rx="1"/><rect x="14" y="14" width="7" height="7" rx="1"/></g></symbol>
    <symbol id="icon-handshake" viewBox="0 0 24 24"><g fill="none" stroke="#fff" stroke-width="1.4" stroke-linejoin="round" stroke-linecap="round"><circle cx="12" cy="4" r="2"/><path d="M2 12l5-3 4 2 3-2 5 2 3 1M7 9l-3 7 4 4 7-4M11 11l-3 3M14 13l-2 2"/></g></symbol>
    <symbol id="icon-team" viewBox="0 0 24 24"><g fill="none" stroke="#fff" stroke-width="1.4"><circle cx="12" cy="4" r="2.5"/><circle cx="6" cy="12" r="2.5"/><circle cx="12" cy="13" r="2.5"/><circle cx="18" cy="12" r="2.5"/><path d="M2 21c0-3 2-5 4-5s4 2 4 5M8 22c0-3 2-5 4-5s4 2 4 5M14 21c0-3 2-5 4-5s4 2 4 5"/></g></symbol>
    <symbol id="icon-heart" viewBox="0 0 24 24"><g fill="none" stroke="#fff" stroke-width="1.4" stroke-linejoin="round" stroke-linecap="round"><path d="M12 21S2 14 2 8a5 5 0 0 1 10-1 5 5 0 0 1 10 1c0 6-10 13-10 13z"/><path d="M7 12l4-2 3 2 3-1M9 14l3 2M11 12l3 2"/></g></symbol>
    <symbol id="icon-open" viewBox="0 0 24 24"><g fill="none" stroke="#fff" stroke-width="1.4" stroke-linejoin="round" stroke-linecap="round"><path d="M12 21S2 14 2 8a5 5 0 0 1 10-1 5 5 0 0 1 10 1c0 6-10 13-10 13z"/><path d="M8 16l4-6 3 1M10 17l5-5"/></g></symbol>
    <symbol id="icon-shield" viewBox="0 0 24 24"><g fill="none" stroke="#fff" stroke-width="1.4" stroke-linejoin="round"><path d="M4 3h16v9c0 5-4 8-8 10-4-2-8-5-8-10z"/><path d="M4 8h16"/><path d="M10 11h4v3h3v3h-3v3h-4v-3H7v-3h3z"/></g></symbol>
  </defs>
</svg>

<!-- Portrait poster -->
<section class="poster poster--portrait">
  <svg class="poster__deco" viewBox="0 0 342 528" aria-hidden="true">
    <path d="M0 52 L40 52 L190 165 L170 200 L0 90 Z" fill="var(--soft-green)" opacity=".8"/>
    <path d="M0 70 L10 60 L180 190 L150 215 L0 110 Z" fill="var(--soft-green)" opacity=".5"/>
    <line x1="300" y1="150" x2="170" y2="260" stroke="var(--soft-lilac)" stroke-width="34" stroke-linecap="round" opacity=".85"/>
  </svg>
  <svg class="poster__deco" viewBox="0 0 342 528" role="img" aria-label="Photo of a construction site with a tower crane and workers in hi-vis at sunset">
    <polygon points="180,0 342,0 342,222" fill="url(#site-photo)"/>
  </svg>

  <div class="brand"><span class="brand__mark"></span><span class="brand__name">CORVELLA<br>Group</span></div>
  <div class="tagline">CONSTRUCTION &amp; ENVIRONMENTAL</div>
  <h1 class="headline">Management<br>Company</h1>
  <p class="intro">We provide industry-leading solutions across traffic management, civil construction, demolition and asbestos, transport and logistics, and environmental management</p>

  <article class="value tone-1" style="top:193px"><div class="value__link"></div><div class="value__pill"><h2 class="value__title">Show<br>Initiative</h2><p class="value__text">We celebrate and recognize our own and encourage forward thinking.</p><svg class="value__icon"><use href="#icon-flag"/></svg></div><span class="value__hook"></span><div class="value__badge">1</div></article>
  <article class="value tone-2" style="top:248px"><div class="value__link"></div><div class="value__pill"><h2 class="value__title">Be<br>Loyal</h2><p class="value__text">We take care of our own and provide opportunities to listen and support each other.</p><svg class="value__icon"><use href="#icon-handshake"/></svg></div><span class="value__hook"></span><div class="value__badge">2</div></article>
  <article class="value tone-3" style="top:303px"><div class="value__link"></div><div class="value__pill"><h2 class="value__title">Think<br>Team</h2><p class="value__text">We communicate effectively and work as a team by helping and supporting each other.</p><svg class="value__icon"><use href="#icon-team"/></svg></div><span class="value__hook"></span><div class="value__badge">3</div></article>
  <article class="value tone-4" style="top:358px"><div class="value__link"></div><div class="value__pill"><h2 class="value__title">Show<br>Respect</h2><p class="value__text">We value the diversity and opinions of all.</p><svg class="value__icon"><use href="#icon-heart"/></svg></div><span class="value__hook"></span><div class="value__badge">4</div></article>
  <article class="value tone-5" style="top:413px"><div class="value__link"></div><div class="value__pill"><h2 class="value__title">Be Open<br>and Honest</h2><p class="value__text">We are clear and open with each other, and provide an approachable and friendly environment.</p><svg class="value__icon"><use href="#icon-open"/></svg></div><span class="value__hook"></span><div class="value__badge">5</div></article>
  <article class="value tone-6" style="top:468px"><div class="value__link"></div><div class="value__pill"><h2 class="value__title">Be<br>Positive</h2><p class="value__sub">Smile</p><p class="value__text">We are solutions focused and encourage a positive attitude turning a negative into a positive.</p><svg class="value__icon"><use href="#icon-shield"/></svg></div><span class="value__hook"></span><div class="value__badge">6</div></article>
</section>

<!-- Landscape poster -->
<section class="poster poster--landscape">
  <svg class="poster__deco" viewBox="0 0 529 342" aria-hidden="true">
    <line x1="150" y1="-10" x2="370" y2="320" stroke="var(--soft-lilac)" stroke-width="40" stroke-linecap="round" opacity=".9"/>
    <path d="M262 40 L290 40 L320 80 L280 90 Z" fill="var(--soft-green)" opacity=".8"/>
    <path d="M305 110 L335 110 L355 160 L310 165 Z" fill="var(--soft-green)" opacity=".8"/>
    <path d="M340 185 L380 185 L400 215 L345 220 Z" fill="var(--soft-green)" opacity=".8"/>
  </svg>
  <svg class="poster__deco" viewBox="0 0 529 342" role="img" aria-label="Photo of a construction site with a tower crane and workers in hi-vis at sunset">
    <polygon points="250,0 529,0 529,95 420,215" fill="url(#site-photo)"/>
  </svg>

  <div class="brand"><span class="brand__mark"></span><span class="brand__name">CORVELLA<br>Group</span></div>

  <article class="value tone-1" style="top:20px"><div class="value__link"></div><div class="value__pill"><h2 class="value__title">Show<br>Initiative</h2><p class="value__text">We celebrate and recognize our own and encourage forward thinking.</p><svg class="value__icon"><use href="#icon-flag"/></svg></div><span class="value__hook"></span><div class="value__badge">1</div></article>
  <article class="value tone-2" style="top:72px"><div class="value__link"></div><div class="value__pill"><h2 class="value__title">Be<br>Loyal</h2><p class="value__text">We take care of our own and provide opportunities to listen and support each other.</p><svg class="value__icon"><use href="#icon-handshake"/></svg></div><span class="value__hook"></span><div class="value__badge">2</div></article>
  <article class="value tone-3" style="top:124px"><div class="value__link"></div><div class="value__pill"><h2 class="value__title">Think<br>Team</h2><p class="value__text">We communicate effectively and work as a team by helping and supporting each other.</p><svg class="value__icon"><use href="#icon-team"/></svg></div><span class="value__hook"></span><div class="value__badge">3</div></article>
  <article class="value tone-4" style="top:176px"><div class="value__link"></div><div class="value__pill"><h2 class="value__title">Show<br>Respect</h2><p class="value__text">We value the diversity and opinions of all.</p><svg class="value__icon"><use href="#icon-heart"/></svg></div><span class="value__hook"></span><div class="value__badge">4</div></article>
  <article class="value tone-5" style="top:228px"><div class="value__link"></div><div class="value__pill"><h2 class="value__title">Be Open<br>and Honest</h2><p class="value__text">We are clear and open with each other, and provide an approachable and friendly environment.</p><svg class="value__icon"><use href="#icon-open"/></svg></div><span class="value__hook"></span><div class="value__badge">5</div></article>
  <article class="value tone-6" style="top:280px"><div class="value__link"></div><div class="value__pill"><h2 class="value__title">Be<br>Positive</h2><p class="value__sub">Smile</p><p class="value__text">We are solutions focused and encourage a positive attitude turning a negative into a positive.</p><svg class="value__icon"><use href="#icon-shield"/></svg></div><span class="value__hook"></span><div class="value__badge">6</div></article>

  <div class="tagline">CONSTRUCTION &amp; ENVIRONMENTAL</div>
  <h1 class="headline">Management<br>Company</h1>
  <p class="intro">We provide industry-leading solutions across traffic management, civil construction, demolition and asbestos, transport and logistics, and environmental management</p>
</section>

</body>
</html>
```